Logo and Business Card Design

Harbor Crest Logistics provides our customers with one call solutions to packing, trucking and warehousing needs throughout the supply chain.
We need ideas for a logo/business card. I have 2 general concepts.
1. Modern logo involving: the globe, Harbor Crest, arrow, movement, the two words having 2 different fonts/colors, the number 1.
2. Logo involving Lion/Winged Lion: incorporate lion onto globe, tagline "The Pride of the Pack", movement, flowing.

Target Market(s)

International Logistics companies, Air cargo companies, manufacturing companies

Industry/Entity Type

Business

Contact Information for Business Card

Dale Verhoeven
Owner
Harbor Crest Logistics
2874 Wexley Blvd.
Elk Grove Village, IL 60219
555-308-2946
daleh@harborcrestfreight.example

Font styles to use
Sans Serif

Requirements
Must have
• 1. Modern logo involving: the globe, Harbor Crest, arrow, movement, the two words having 2 different fonts/colors, the number 1.
Nice to have
Should not have
• Do not have too complex of a design.

```html
<!DOCTYPE html>
<html lang="en">
<head>
<meta charset="utf-8">
<title>Harbor Crest Logistics – Business Card</title>
<link rel="stylesheet" href="https://fonts.googleapis.com/css2?family=Open+Sans:wght@400;600;700&display=swap">
<style>
  :root {
    --page-bg: #e9ebee;
    --card-bg: #ffffff;
    --card-shade: #eef0f3;
    --brand-blue: #2f5fc4;
    --brand-deep: #1f3fae;
    --brand-light: #2a8fe0;
    --text-dark: #3a3a3a;
    --rule: #9a9a9a;
    --white: #ffffff;
  }
  * { box-sizing: border-box; margin: 0; padding: 0; }
  html, body { width: 1200px; height: 899px; overflow: hidden; }
  body {
    background: var(--page-bg);
    font-family: "Open Sans", sans-serif;
    position: relative;
  }
  .card {
    position: absolute;
    width: 560px;
    height: 320px;
    background: linear-gradient(135deg, var(--card-bg) 40%, var(--card-shade));
    box-shadow: 0 8px 24px rgba(0,0,0,.18);
    overflow: hidden;
  }
  .card--front { left: 190px; top: 70px; }
  .card--back  { left: 450px; top: 480px; }

  .logo {
    position: absolute;
    display: flex;
    align-items: center;
    gap: 12px;
  }
  .logo__mark {
    width: 34px; height: 34px;
    background: var(--brand-blue);
  }
  .logo__name {
    font-weight: 700;
    color: var(--brand-blue);
    letter-spacing: 1px;
    text-transform: uppercase;
    line-height: 1;
  }
  .card--front .logo { left: 50%; top: 50%; transform: translate(-50%, -50%); }
  .card--front .logo__name { font-size: 40px; }
  .card--back .logo { left: 60px; top: 108px; }
  .card--back .logo__mark { width: 26px; height: 26px; }
  .card--back .logo__name { font-size: 28px; }

  .contact {
    position: absolute;
    left: 318px; top: 28px;
    padding-left: 12px;
    border-left: 1px solid var(--rule);
    font-size: 11.5px;
    line-height: 1.45;
    color: var(--text-dark);
  }
  .contact__address { margin-bottom: 2px; }
  .contact__row { display: flex; align-items: center; gap: 6px; }
  .contact__row svg { width: 11px; height: 11px; flex: none; fill: var(--text-dark); }

  .wave { position: absolute; left: 0; top: 0; width: 560px; height: 320px; }
  .holder {
    position: absolute;
    left: 70px; top: 272px;
    font-size: 12px;
    letter-spacing: 2.5px;
    color: var(--white);
    text-transform: uppercase;
  }
  .holder__title { text-transform: none; letter-spacing: 1.5px; }
</style>
</head>
<body>

<section class="card card--front" aria-label="Card front">
  <div class="logo">
    <span class="logo__mark"></span>
    <span class="logo__name">Harbor Crest</span>
  </div>
</section>

<section class="card card--back" aria-label="Card back">
  <svg class="wave" viewBox="0 0 560 320" aria-hidden="true">
    <defs>
      <linearGradient id="waveFill" x1="0" y1="0" x2="1" y2="0">
        <stop offset="0" stop-color="#2d4fc2"/>
        <stop offset="0.5" stop-color="#2a8fe0"/>
        <stop offset="1" stop-color="#1f3fae"/>
      </linearGradient>
    </defs>
    <path d="M0 248 C150 262 360 230 560 108 L560 320 L0 320 Z" fill="url(#waveFill)"/>
    <path d="M0 238 C170 250 370 220 560 98" fill="none" stroke="#2a6fd6" stroke-width="3"/>
    <path d="M0 254 C170 266 380 230 560 116" fill="none" stroke="#ffffff" stroke-width="4"/>
  </svg>

  <div class="logo">
    <span class="logo__mark"></span>
    <span class="logo__name">Harbor Crest</span>
  </div>

  <address class="contact" style="font-style:normal">
    <div class="contact__address">2874 Wexley Blvd.<br>Elk Grove Village, IL 60219</div>
    <div class="contact__row">
      <svg viewBox="0 0 24 24"><path d="M6.6 10.8a15 15 0 0 0 6.6 6.6l2.2-2.2a1 1 0 0 1 1-.25 11.4 11.4 0 0 0 3.6.6 1 1 0 0 1 1 1V20a1 1 0 0 1-1 1A17 17 0 0 1 3 4a1 1 0 0 1 1-1h3.5a1 1 0 0 1 1 1 11.4 11.4 0 0 0 .6 3.6 1 1 0 0 1-.25 1z"/></svg>
      <span>555-308-2946</span>
    </div>
    <div class="contact__row">
      <svg viewBox="0 0 24 24"><path d="M2 5h20v14H2z M2 5l10 8 10-8" fill="none" stroke="#3a3a3a" stroke-width="2"/></svg>
      <span>daleh@harborcrestfreight.example</span>
    </div>
    <div class="contact__row">
      <svg viewBox="0 0 24 24"><circle cx="12" cy="12" r="10" fill="none" stroke="#3a3a3a" stroke-width="2"/><path d="M2 12h20M12 2c3 3 3 17 0 20M12 2c-3 3-3 17 0 20" fill="none" stroke="#3a3a3a" stroke-width="1.6"/></svg>
      <span>www.harborcrestfreight.example</span>
    </div>
  </address>

  <p class="holder">Dale Verhoeven <span class="holder__title">Managing Director</span></p>
</section>

</body>
</html>
```